Flyer Design Project

I teach a spiritual dance class and I want to explain what it is and who it would benefit. I would love to have a sticker for where I am teaching it because that can change.

I want it to be a bit spiritual, very hip and cool, and transformational!!

Target Market(s)

Mostly women (or enlightened men)! all ages

Requirements
Must have
• Lumen Sway

We need to move. We need to breathe. We need to smile and giggle and laugh and cry and scream and make noise and dance. It's not about burning calories and it is not about reaching a goal. It's about feeling. It's about taking the time to nurture our souls. It's about finding joy and peace in our hectic lives. It's about healing.

Lumen Sway is a wildly fun, uplifting, emotionally cleansing, refreshing, restorative, heart-opening, transformational dance celebration that is sure to leave you relaxed and smiling. All ages, shapes and sizes are welcome with no experience necessary.
About Carla:

I was certified at Vestora in both “Open Heart Motion Flow” and “Tidal Steps” and am a
certified Group Exercise Instructor with the National Council for Active Movement Trainers (NCAM). I also have a black belt in Tae Kwon Do. As of 2013, I will be a certified holistic health and nutrition coach and am the creator of the popular Bright, Bold, and Breezy page on Friendloop.
For more info:
Carlabrennick@mailvista.net

Classes and workshops to energize your body, mind, and spirit.

```html
<!DOCTYPE html>
<html lang="en">
<head>
<meta charset="utf-8">
<title>Lumen Sway – Flyer</title>
<link rel="stylesheet" href="https://fonts.googleapis.com/css2?family=Amaranth:wght@400;700&family=Fredoka:wght@500;600&display=swap">
<style>
  :root {
    --backdrop: #3a3a3a;
    --sky-top: #eaf6fd;
    --sky-mid: #bfe3f8;
    --sky-low: #a9d8f4;
    --paper: #ffffff;
    --swoosh: #2fa9de;
    --sun: #ffc21a;
    --lime: #9fd63a;
    --magenta: #e6127f;
    --ink: #111111;
    --rule: rgba(255,255,255,0.9);
  }
  * { box-sizing: border-box; margin: 0; padding: 0; }
  html, body { width: 1200px; height: 900px; overflow: hidden; }
  body {
    background: var(--backdrop);
    display: flex; align-items: center; justify-content: center;
    font-family: "Amaranth", "Trebuchet MS", sans-serif;
    color: var(--ink);
  }
  .flyer {
    position: relative;
    width: 660px; height: 854px;
    overflow: hidden;
    background: linear-gradient(180deg, var(--sky-top) 0%, var(--sky-mid) 45%, var(--sky-low) 100%);
    box-shadow: 0 8px 30px rgba(0,0,0,0.45);
  }
  .flyer__backdrop { position: absolute; inset: 0; width: 660px; height: 854px; }

  .art { position: absolute; }
  .art--sun {
    right: -60px; top: -40px; width: 260px; height: 260px; border-radius: 50%;
    background: radial-gradient(circle, #fff7a8 0%, #ffe36a 45%, rgba(255,200,60,0) 72%);
  }
  .art--petals {
    right: 20px; top: 150px; width: 260px; height: 230px; border-radius: 50% 50% 45% 55%;
    background: radial-gradient(ellipse at 45% 55%, rgba(255,120,70,0.85) 0%, rgba(255,170,110,0.6) 50%, rgba(255,190,140,0) 75%);
  }
  .art--dancer {
    left: 445px; top: 12px; width: 120px; height: 300px; border-radius: 60px 60px 30px 30px;
    background: linear-gradient(180deg, #ec1482, #e6127f);
  }
  .art--lotus {
    left: 30px; top: 470px; width: 320px; height: 230px; border-radius: 50% 50% 40% 40%;
    background: radial-gradient(ellipse at 50% 60%, rgba(80,160,230,0.55) 0%, rgba(110,184,234,0.3) 50%, rgba(110,184,234,0) 75%);
  }
  .art--leaves {
    right: -40px; bottom: -40px; width: 340px; height: 300px; border-radius: 50%;
    background: radial-gradient(ellipse at 60% 60%, rgba(170,230,90,0.85) 0%, rgba(200,240,130,0.55) 45%, rgba(200,240,130,0) 72%);
  }

  .brand {
    position: absolute; left: 34px; top: 90px;
    font-family: "Fredoka", "Arial Rounded MT Bold", sans-serif;
    font-weight: 600; font-size: 64px; line-height: 1;
    color: var(--sun); letter-spacing: 1px; white-space: nowrap;
  }
  .tagline {
    position: absolute; left: 56px; top: 178px; width: 340px;
    font-weight: 700; font-size: 20px; line-height: 1.25; color: var(--magenta);
  }
  .manifesto { position: absolute; left: 34px; top: 330px; width: 600px; }
  .manifesto__lead { font-weight: 700; font-size: 19px; line-height: 1.3; }
  .manifesto__body { margin-top: 16px; font-size: 14px; line-height: 1.3; }

  .column { position: absolute; top: 478px; }
  .column--about { left: 34px; width: 290px; }
  .column--host { left: 348px; width: 280px; }
  .column__heading {
    font-family: "Fredoka", "Arial Rounded MT Bold", sans-serif;
    font-weight: 500; font-size: 22px; color: var(--magenta);
    text-transform: uppercase; padding-bottom: 6px;
    border-bottom: 2px solid var(--rule); margin-bottom: 12px;
  }
  .column--about .column__text { font-size: 16px; line-height: 1.28; }
  .column--host .column__text { font-size: 14px; line-height: 1.3; }

  .venue { position: absolute; left: 34px; top: 722px; width: 590px; }
  .venue__label { font-weight: 700; font-size: 17px; }
  .venue__sticker { margin-top: 10px; height: 44px; border-radius: 12px; background: var(--paper); }

  .contact {
    position: absolute; left: 34px; top: 812px;
    display: flex; align-items: center; gap: 6px;
    font-weight: 700; font-size: 17px;
  }
  .contact__dot { width: 13px; height: 13px; border-radius: 50%; background: var(--sun); }
  .contact__email { color: var(--magenta); }
</style>
</head>
<body>
  <main class="flyer">
    <svg class="flyer__backdrop" viewBox="0 0 660 854" aria-hidden="true">
      <path d="M0 0 H660 V60 C560 230 330 320 0 300 Z" fill="var(--paper)"/>
    </svg>
    <div class="art art--sun" role="img" aria-label="Glowing yellow sun"></div>
    <div class="art art--petals" role="img" aria-label="Large orange flower petals"></div>
    <div class="art art--lotus" role="img" aria-label="Soft blue lotus shape"></div>
    <div class="art art--leaves" role="img" aria-label="Green leaves"></div>
    <svg class="flyer__backdrop" viewBox="0 0 660 854" aria-hidden="true">
      <path d="M0 290 C250 330 470 270 660 130" fill="none" stroke="var(--swoosh)" stroke-width="14" stroke-linecap="round" opacity="0.85"/>
      <circle cx="36" cy="270" r="9" fill="var(--sun)"/>
      <circle cx="20" cy="288" r="4" fill="var(--lime)"/>
      <circle cx="600" cy="268" r="24" fill="var(--sun)"/>
      <circle cx="590" cy="228" r="9" fill="var(--lime)"/>
      <circle cx="612" cy="204" r="5" fill="var(--lime)"/>
    </svg>
    <div class="art art--dancer" role="img" aria-label="Magenta silhouette of a dancing woman with arm raised"></div>

    <h1 class="brand">Lumen Sway</h1>
    <p class="tagline">Classes and workshops to energize your body, mind, and spirit.</p>

    <section class="manifesto">
      <p class="manifesto__lead">We need to move. We need to breathe. We need to smile and giggle and laugh and cry and scream and make noise and dance.</p>
      <p class="manifesto__body">It's not about burning calories and it is not about reaching a goal. It's about feeling. It's about taking the time to nurture our souls. It's about finding joy and peace in our hectic lives. It's about <strong>healing.</strong></p>
    </section>

    <section class="column column--about">
      <h2 class="column__heading">About Lumen Sway</h2>
      <p class="column__text">Lumen Sway is a wildly fun, uplifting, emotionally cleansing, refreshing, restorative, heart-opening, transformational dance celebration that is sure to leave you relaxed and smiling. All ages, shapes and sizes are welcome with no experience necessary.</p>
    </section>

    <section class="column column--host">
      <h2 class="column__heading">About Carla</h2>
      <p class="column__text">I was certified at Vestora in both “Open Heart Motion Flow” and “Tidal Steps” and am a certified Group Exercise Instructor with the National Council for Active Movement Trainers (NCAM). I also have a black belt in Tae Kwon Do. As of 2013, I will be a certified holistic health and nutrition coach and am the creator of the popular Bright, Bold, and Breezy page on Friendloop.</p>
    </section>

    <section class="venue">
      <p class="venue__label">Classes are located at:</p>
      <div class="venue__sticker"></div>
    </section>

    <p class="contact"><span class="contact__dot"></span>For more info: <span class="contact__email">Carlabrennick@mailvista.net</span></p>
  </main>
</body>
</html>
```